Dietitian needs a new business card design

I need a new business card design for my nutrition business that provides individual clinical nutrition advice for people with medical conditions. Business cards will be handed out to doctors, specialists and clients so will need to be sharp and project an image of professionalism

Target Market(s)

My clients are typically referred by doctors or specialists and the card will be used to handout to clients and their doctors.

Industry/Entity Type

Medical

Contact Information for Business Card

The business card will require the details below. These details can be found from my website https://www.kelvarrowclinic.com.au/

Font styles to use
Serif

Colors

Designer to choose colors to be used in the design.

Requirements
Must have
• 1. It needs be professional and contemporary
• 2. It needs to incorporate my logo
• 3. It needs space to write appointment times and dates
• 4. It needs to provide my phone number, fax number, email address and my web address
Nice to have
• Include the Registered Tovance Clinician Logo
• I have access to Framellow if required
• The locations I practise from
Should not have
• Pictures of food
• Spelling MIstakes

```html
<!DOCTYPE html>
<html lang="en">
<head>
<meta charset="utf-8">
<title>Kelvarrow Nutrition &amp; Dietetics – Business Card</title>
<link rel="stylesheet" href="https://fonts.googleapis.com/css2?family=Arimo:wght@400;700&family=Pathway+Gothic+One&display=swap">
<style>
  :root {
    --ink: #000000;
    --paper: #ffffff;
    --accent-yellow: #f5f200;
    --alert-red: #ff0000;
    --icon-violet: #5a1fe0;
    --icon-green: #1f8a3e;
    --social-purple: #7b3aa6;
    --social-blue: #14589c;
    --badge-orange: #f07a23;
    --brand-navy: #1f3f93;
  }
  * { margin: 0; padding: 0; box-sizing: border-box; }
  html, body { width: 1200px; height: 1200px; overflow: hidden; background: var(--paper); }
  body { position: relative; font-family: "Arimo", Arial, sans-serif; color: var(--ink); }

  .card-shapes { position: absolute; left: 0; top: 0; width: 1200px; height: 1200px; }

  .abs { position: absolute; white-space: nowrap; }

  .brand-name {
    font-family: "Arimo", Arial, sans-serif;
    font-weight: 400;
    font-size: 15px;
    color: var(--brand-navy);
    line-height: 1.15;
  }

  .contact-line { font-size: 30px; line-height: 1; }
  .contact-email { font-size: 29px; line-height: 1; }
  .contact-email .address { font-family: "Pathway Gothic One", "Arial Narrow", sans-serif; font-size: 33px; }

  .holder-name { font-size: 53px; font-weight: 700; line-height: 1; }
  .holder-credentials { font-size: 26px; line-height: 1; }

  .location { line-height: 1; }
  .location p { white-space: nowrap; }
  .location-lg p { font-size: 24px; height: 25px; }
  .location-xl p { font-size: 25px; height: 26.5px; }
  .location-sm p { font-size: 21.5px; height: 23px; }
  .location-md p { font-size: 22px; height: 24px; }
</style>
</head>
<body>

<svg class="card-shapes" viewBox="0 0 1500 1500" aria-hidden="true">
  <!-- front card -->
  <rect x="166" y="14" width="1063" height="57" fill="var(--ink)"/>
  <rect x="166" y="607" width="1063" height="57" fill="var(--ink)"/>
  <polyline points="397,70 497,338 397,607" fill="none" stroke="var(--ink)" stroke-width="7"/>
  <polyline points="493,70 595,338 493,607" fill="none" stroke="var(--accent-yellow)" stroke-width="7"/>

  <rect x="238" y="130" width="72" height="72" fill="var(--alert-red)"/>

  <circle cx="222" cy="313" r="34" fill="var(--brand-navy)"/>

  <rect x="197" y="428" width="195" height="90" rx="3" fill="var(--badge-orange)"/>
  <circle cx="345" cy="473" r="37" fill="var(--paper)"/>

  <!-- phone -->
  <circle cx="604" cy="136" r="48" fill="var(--ink)"/>
  <polygon points="604,88 635,88 686,184 604,184" fill="var(--ink)"/>
  <circle cx="604" cy="136" r="35" fill="var(--icon-violet)"/>
  <path d="M592 116 q-8 4 -6 16 q4 20 24 30 q10 2 14 -6 l-8 -8 q-4 4 -8 2 q-10 -6 -14 -16 q-2 -4 2 -8 z" fill="var(--paper)"/>

  <!-- fax -->
  <circle cx="651" cy="273" r="48" fill="var(--ink)"/>
  <polygon points="651,225 682,225 733,321 651,321" fill="var(--ink)"/>
  <circle cx="651" cy="273" r="35" fill="var(--icon-violet)"/>
  <path d="M639 253 q-8 4 -6 16 q4 20 24 30 q10 2 14 -6 l-8 -8 q-4 4 -8 2 q-10 -6 -14 -16 q-2 -4 2 -8 z" fill="var(--paper)"/>

  <!-- email -->
  <circle cx="645" cy="408" r="50" fill="var(--ink)"/>
  <polygon points="645,358 727,358 673,458 645,458" fill="var(--ink)"/>
  <circle cx="645" cy="408" r="36" fill="var(--icon-green)"/>
  <rect x="624" y="395" width="42" height="27" fill="none" stroke="var(--paper)" stroke-width="3"/>
  <polyline points="624,395 645,412 666,395" fill="none" stroke="var(--paper)" stroke-width="3"/>

  <!-- social -->
  <circle cx="734" cy="542" r="53" fill="var(--social-purple)"/>
  <circle cx="941" cy="542" r="54" fill="var(--social-blue)"/>

  <!-- back card -->
  <rect x="166" y="769" width="1063" height="57" fill="var(--ink)"/>
  <rect x="166" y="1362" width="1063" height="57" fill="var(--ink)"/>
  <circle cx="272" cy="904" r="34" fill="var(--brand-navy)"/>

  <rect x="228" y="1022" width="6" height="278" rx="3" fill="var(--ink)"/>
  <rect x="734" y="1022" width="6" height="161" rx="3" fill="var(--ink)"/>
  <rect x="734" y="1207" width="6" height="109" rx="3" fill="var(--ink)"/>
</svg>

<!-- front card text -->
<div class="abs brand-name" style="left:212px; top:234px;">Kelvarrow<br>Nutrition &amp; Dietetics</div>

<div class="abs contact-line" style="left:546px; top:97px;">Tel: 0491 552 307</div>
<div class="abs contact-line" style="left:586px; top:204px;">Fax: +613 6390 4417</div>
<div class="abs contact-email" style="left:550px; top:313px;">Email:<span class="address">martin@kelvarrowclinic.com.au</span></div>

<!-- back card text -->
<div class="abs brand-name" style="left:253px; top:706px;">Kelvarrow<br>Nutrition &amp; Dietetics</div>

<div class="abs holder-name" style="left:422px; top:688px;">Martin Calloway</div>
<div class="abs holder-credentials" style="left:421px; top:750px;">BHlthSc, MND, APD</div>

<div class="abs location location-lg" style="left:209px; top:813px;">
  <p>Brindlemoor Doctors Surgery</p>
  <p>14 Harlow Road</p>
  <p>Brindlemoor Tasmania</p>
  <p>brindlemoordoctors.com.au</p>
  <p>Next Visit 2nd November 2018</p>
</div>

<div class="abs location location-xl" style="left:209px; top:951px;">
  <p>Ashvale Health</p>
  <p>9 Corrin Drive</p>
  <p>Ashvale Tasmania</p>
  <p>7391</p>
  <p>ashvalehealth.com.au</p>
</div>

<div class="abs location location-sm" style="left:613px; top:815px;">
  <p>Fernhurst Medical Centre</p>
  <p>Cnr Lyle &amp; Garnet Streets</p>
  <p>Westbrook</p>
  <p>Calderton Tasmania</p>
  <p>7391</p>
  <p>fernhurstmedical.com.au</p>
</div>

<div class="abs location location-md" style="left:613px; top:962px;">
  <p>Quorran Medical</p>
  <p>5/118 Tolley Road</p>
  <p>Quorran Tasmania</p>
  <p>7391</p>
</div>

</body>
</html>
```